Power point Presentation Template 2

I am looking a professionally designed Powerpoint Presentation template for my company. We are Information Technology Company. I have attached the Logo. The Logo will also give an indication of which colours to be used in the design.

Information and Communication Technology

• All ideas welcomed
• Professional Look and Feel

```html
<!DOCTYPE html>
<html lang="en">
<head>
<meta charset="utf-8">
<title>Nexora Technologies – Presentation Template Overview</title>
<link href="https://fonts.googleapis.com/css2?family=Lato:wght@400;700;900&family=Open+Sans:wght@400&display=swap" rel="stylesheet">
<style>
:root{
  --orange:#f7901e;
  --orange-deep:#ee7a0b;
  --orange-soft:#fbc58b;
  --dark:#555a5f;
  --ink:#4a4a4a;
  --body:#707070;
  --light:#d3d3d3;
  --paper:#ffffff;
  --canvas:#e6e6e6;
  --label:#3c3c3c;
  --select:#d24726;
  --green:#72b043;
}
*{box-sizing:border-box;margin:0;padding:0}
html,body{width:1200px;height:559px;overflow:hidden;background:var(--canvas)}
body{font-family:"Open Sans",sans-serif}
.sorter{display:grid;grid-template-columns:repeat(8,118px);column-gap:30.5px;grid-auto-rows:112.5px;padding:9px 0 0 18px}
.cell{position:relative}
.slide{position:relative;width:118px;height:67px;background:var(--paper);border:1px solid #c9c9c9;overflow:hidden;font-family:"Lato",sans-serif}
.slide.current{border:2px solid #8a8a8a}
.slide.selected{outline:2px solid var(--select);outline-offset:1px}
.caption{display:flex;justify-content:space-between;width:118px;margin-top:5px;font-size:12.5px;color:var(--label);line-height:1}
.caption.selected .num{color:var(--select)}
.meta{font-size:11.5px}
.abs{position:absolute}
.title{position:absolute;left:5px;top:4px;font-weight:700;font-size:4.6px;color:var(--orange);white-space:nowrap}
.topline{position:absolute;left:5px;right:5px;top:11px;height:.5px;background:var(--orange-soft)}
.brand{position:absolute;top:3px;right:4px;font-weight:900;font-size:4px;color:var(--orange);letter-spacing:.2px;display:flex;align-items:center;gap:1px}
.brand::before{content:"";width:3px;height:3px;background:currentColor}
.brand.light{color:#fff}
.brand.big{font-size:7px;gap:2px}
.brand.big::before{width:5px;height:5px}
.foot{position:absolute;left:5px;right:5px;bottom:3px;height:.5px;background:#ddd}
.foot::before{content:"";position:absolute;left:0;top:-.3px;width:18px;height:1px;background:var(--orange)}
.p{position:absolute;font-family:"Open Sans",sans-serif;font-size:1.9px;line-height:2.8px;color:var(--body);overflow:hidden;text-align:justify}
.p.w{color:#fff}
.p.c{text-align:center}
.h{display:block;font-family:"Lato",sans-serif;font-weight:700;font-size:2.4px;line-height:3.2px;color:var(--ink);text-align:inherit}
.h.o{color:var(--orange)}
.h.w{color:#fff}
.photo-desk{background:linear-gradient(160deg,#eef0ee 0%,#d9dcd8 45%,#b9bfb6 100%)}
.photo-net{background:radial-gradient(circle at 30% 45%,#d6c6e0 0%,#5a6f8f 25%,#2f3f58 70%,#22303f 100%)}
.photo-net-grey{background:radial-gradient(circle at 35% 45%,#e2e2e2 0%,#8d8d8d 35%,#555 100%)}
.photo-office{background:linear-gradient(120deg,#c8b9a6 0%,#e7e1d8 40%,#b6a68f 100%)}
.photo-phone{background:linear-gradient(#f0e2d2,#caa88a)}
.hero-text{position:absolute;color:#fff;font-weight:900}
.sq{position:absolute;background:var(--orange)}
.circ{position:absolute;border-radius:50%}
.ico{position:absolute}
</style>
</head>
<body>
<main class="sorter">

<!-- 1 -->
<div class="cell"><div class="slide">
  <div class="abs photo-desk" style="inset:0" role="img" aria-label="Photo of potted plants on a bright office desk"></div>
  <div class="abs" style="left:0;right:0;top:33px;height:27px;background:rgba(247,144,30,.88)"></div>
  <div class="hero-text" style="left:12px;top:38px;font-size:7px">TITLE PAGE</div>
  <div class="hero-text" style="left:12px;top:47px;font-size:3px;font-weight:400">YOUR TEXT IS HERE</div>
  <div class="brand big light" style="top:42px;right:12px">NEXORA</div>
</div><div class="caption"><span class="num">1</span></div></div>

<!-- 2 -->
<div class="cell"><div class="slide">
  <div class="brand big" style="top:13px;left:30px;right:auto">NEXORA</div>
  <div class="title" style="top:40px;font-size:5px">Introduction</div>
  <p class="p" style="left:5px;right:5px;top:48px;height:9px">Our team designs, builds and supports secure information systems for growing businesses. We combine cloud services, smart networks and clear advice so every client can work faster, protect its data and plan the next step with confidence and care.</p>
</div><div class="caption"><span class="num">2</span></div></div>

<!-- 3 -->
<div class="cell"><div class="slide">
  <div class="title">Standard pages</div><div class="brand">NEXORA</div><div class="topline"></div>
  <p class="p" style="left:10px;right:10px;top:15px;height:42px">Our team designs, builds and supports secure information systems for growing businesses. We combine cloud services, smart networks and clear advice so every client can work faster, protect its data and plan the next step with confidence and care. Our team designs, builds and supports secure information systems for growing businesses. We combine cloud services, smart networks and clear advice so every client can work faster, protect its data and plan the next step with confidence and care. Our team designs, builds and supports secure information systems for growing businesses. We combine cloud services, smart networks and clear advice so every client can work faster, protect its data and plan the next step with confidence and care. Our team designs, builds and supports secure information systems for growing businesses. We combine cloud services, smart networks and clear advice so every client can work faster, protect its data and plan the next step with confidence and care.</p>
  <div class="foot"></div>
</div><div class="caption"><span class="num">3</span></div></div>

<!-- 4 -->
<div class="cell"><div class="slide current">
  <div class="title">Standard pages</div><div class="brand">NEXORA</div><div class="topline"></div>
  <p class="p" style="left:10px;width:46px;top:15px;height:42px">Our team designs, builds and supports secure information systems for growing businesses. We combine cloud services, smart networks and clear advice so every client can work faster, protect its data and plan the next step with confidence and care. Our team designs, builds and supports secure information systems for growing businesses. We combine cloud services, smart networks and clear advice so every client can work faster, protect its data and plan the next step with confidence and care.</p>
  <p class="p" style="left:62px;width:46px;top:15px;height:42px">Our team designs, builds and supports secure information systems for growing businesses. We combine cloud services, smart networks and clear advice so every client can work faster, protect its data and plan the next step with confidence and care. Our team designs, builds and supports secure information systems for growing businesses. We combine cloud services, smart networks and clear advice so every client can work faster, protect its data and plan the next step with confidence and care.</p>
  <div class="foot"></div>
</div><div class="caption"><span class="num">4</span></div></div>

<!-- 5 -->
<div class="cell"><div class="slide">
  <div class="title">Standard pages</div><div class="brand">NEXORA</div><div class="topline"></div>
  <p class="p" style="left:10px;width:30px;top:15px;height:43px">Our team designs, builds and supports secure information systems for growing businesses. We combine cloud services, smart networks and clear advice so every client can work faster, protect its data and plan the next step with confidence and care. Our team designs, builds and supports secure information systems for growing businesses. We combine cloud services, smart networks and clear advice so every client can work faster, protect its data and plan the next step with confidence and care.</p>
  <p class="p" style="left:44px;width:30px;top:15px;height:43px">Our team designs, builds and supports secure information systems for growing businesses. We combine cloud services, smart networks and clear advice so every client can work faster, protect its data and plan the next step with confidence and care. Our team designs, builds and supports secure information systems for growing businesses. We combine cloud services, smart networks and clear advice so every client can work faster, protect its data and plan the next step with confidence and care.</p>
  <p class="p" style="left:78px;width:30px;top:15px;height:43px">Our team designs, builds and supports secure information systems for growing businesses. We combine cloud services, smart networks and clear advice so every client can work faster, protect its data and plan the next step with confidence and care. Our team designs, builds and supports secure information systems for growing businesses. We combine cloud services, smart networks and clear advice so every client can work faster, protect its data and plan the next step with confidence and care.</p>
  <div class="foot"></div>
</div><div class="caption"><span class="num">5</span></div></div>

<!-- 6 -->
<div class="cell"><div class="slide">
  <div class="title">Standard pages</div><div class="topline" style="right:50px"></div>
  <p class="p" style="left:5px;width:58px;top:15px;height:20px">Our team designs, builds and supports secure information systems for growing businesses. We combine cloud services, smart networks and clear advice so every client can work faster, protect its data and plan the next step with confidence and care.</p>
  <div class="abs photo-office" style="left:68px;right:0;top:0;bottom:0" role="img" aria-label="Photo of a person writing at a desk"></div>
  <div class="foot" style="right:52px"></div>
</div><div class="caption"><span class="num">6</span></div></div>

<!-- 7 -->
<div class="cell"><div class="slide">
  <div class="abs photo-desk" style="left:0;width:60px;top:0;bottom:0" role="img" aria-label="Photo of potted plants on a desk"></div>
  <div class="abs" style="left:60px;right:0;top:0;bottom:0;background:var(--orange)"></div>
  <div class="hero-text" style="left:64px;top:6px;font-size:4.5px">PAGE TITLE</div>
  <p class="p w" style="left:64px;right:6px;top:14px;height:36px;font-size:2.3px;line-height:3.4px">Our team designs, builds and supports secure information systems for growing businesses. We combine cloud services, smart networks and clear advice so every client can work faster, protect its data and plan the next step with confidence and care.</p>
</div><div class="caption"><span class="num">7</span></div></div>

<!-- 8 -->
<div class="cell"><div class="slide">
  <div class="abs" style="left:0;width:58px;top:0;bottom:0;background:var(--dark)"></div>
  <div class="hero-text" style="left:4px;top:6px;font-size:4.5px">PAGE TITLE</div>
  <p class="p w" style="left:4px;width:50px;top:14px;height:36px;font-size:2.3px;line-height:3.4px">Our team designs, builds and supports secure information systems for growing businesses. We combine cloud services, smart networks and clear advice so every client can work faster, protect its data and plan the next step with confidence and care.</p>
  <div class="abs photo-net" style="left:58px;right:0;top:0;bottom:0" role="img" aria-label="Photo of a hand touching a glowing network graphic"></div>
</div><div class="caption"><span class="num">8</span></div></div>

<!-- 9 -->
<div class="cell"><div class="slide">
  <div class="abs" style="inset:0;background:linear-gradient(90deg,#e4823a,#b8793f 45%,#8f8a86)" role="img" aria-label="Photo of a person in an office, orange toned"></div>
  <div class="abs" style="left:0;right:0;top:30px;height:27px;background:rgba(60,60,60,.75)"></div>
  <div class="hero-text" style="left:10px;top:35px;font-size:7px">TITLE PAGE</div>
  <div class="hero-text" style="left:10px;top:44px;font-size:3px;font-weight:400">YOUR TEXT IS HERE</div>
  <div class="brand big light" style="top:39px;right:14px">NEXORA</div>
</div><div class="caption"><span class="num">9</span></div></div>

<!-- 10 -->
<div class="cell"><div class="slide">
  <div class="abs photo-net" style="left:0;right:0;top:0;height:28px" role="img" aria-label="Banner photo of a hand touching a network graphic"></div>
  <div class="title" style="top:31px;font-size:3.5px">Great Work Facts About Us</div>
  <p class="p" style="left:5px;right:12px;top:36px;height:6px">Our team designs, builds and supports secure information systems for growing businesses. We combine cloud services, smart networks and clear advice so every client can work faster, protect its data and plan the next step with confidence and care.</p>
  <svg class="ico" style="left:7px;top:46px" width="7" height="7" viewBox="0 0 10 10" aria-hidden="true"><circle cx="5" cy="5" r="4.4" fill="none" stroke="var(--dark)" stroke-width=".9"/><path d="M3 5.2 4.5 6.6 7.2 3.6" fill="none" stroke="var(--dark)" stroke-width=".9"/></svg>
  <svg class="ico" style="left:47px;top:46px" width="7" height="7" viewBox="0 0 10 10" aria-hidden="true"><circle cx="5" cy="5" r="4.4" fill="none" stroke="var(--dark)" stroke-width=".9"/><path d="M5 2.6V5l1.8 1.2" fill="none" stroke="var(--dark)" stroke-width=".9"/></svg>
  <svg class="ico" style="left:86px;top:46px" width="7" height="7" viewBox="0 0 10 10" aria-hidden="true"><circle cx="5" cy="5" r="4.4" fill="none" stroke="var(--dark)" stroke-width=".9"/><path d="M3 6.5h4M3.5 6.5V4.5M5 6.5V3.2M6.5 6.5V4" fill="none" stroke="var(--dark)" stroke-width=".8"/></svg>
  <p class="p" style="left:16px;width:24px;top:45px;height:10px"><span class="h">Label</span>Short text about this point goes here in a few words.</p>
  <p class="p" style="left:56px;width:24px;top:45px;height:10px"><span class="h">Label</span>Short text about this point goes here in a few words.</p>
  <p class="p" style="left:95px;width:19px;top:45px;height:10px"><span class="h">Label</span>Short text about this point goes here in a few words.</p>
  <div class="foot"></div>
</div><div class="caption"><span class="num">10</span><span class="meta">★</span></div></div>

<!-- 11 -->
<div class="cell"><div class="slide">
  <div class="title" style="top:9px;left:9px">TEAM PAGE</div>
  <div class="circ" style="left:9px;top:18px;width:19px;height:19px;background:#c7c7c7;border:1.5px solid var(--orange)"></div>
  <div class="circ" style="left:37px;top:18px;width:19px;height:19px;background:#c7c7c7;border:1.5px solid var(--orange)"></div>
  <div class="circ" style="left:65px;top:18px;width:19px;height:19px;background:#c7c7c7;border:1.5px solid #bbb"></div>
  <div class="circ" style="left:93px;top:18px;width:19px;height:19px;background:#c7c7c7;border:1.5px solid #bbb"></div>
  <p class="p c" style="left:8px;width:21px;top:39px;height:16px"><span class="h">Name Here</span>Short text about this point goes here in a few words.</p>
  <p class="p c" style="left:36px;width:21px;top:39px;height:16px"><span class="h">Name Here</span>Short text about this point goes here in a few words.</p>
  <p class="p c" style="left:64px;width:21px;top:39px;height:16px"><span class="h">Name Here</span>Short text about this point goes here in a few words.</p>
  <p class="p c" style="left:92px;width:21px;top:39px;height:16px"><span class="h">Name Here</span>Short text about this point goes here in a few words.</p>
</div><div class="caption"><span class="num">11</span><span class="meta">★ 00:00</span></div></div>

<!-- 12 -->
<div class="cell"><div class="slide">
  <div class="title">List Layout</div><div class="brand">NEXORA</div><div class="topline"></div>
  <div class="abs" style="left:8px;top:16px;width:22px;height:3.5px;background:var(--orange)"></div>
  <div class="abs" style="left:35px;top:16px;width:22px;height:3.5px;background:var(--dark)"></div>
  <div class="abs" style="left:62px;top:16px;width:22px;height:3.5px;background:var(--dark)"></div>
  <div class="abs" style="left:89px;top:16px;width:22px;height:3.5px;background:var(--dark)"></div>
  <div class="abs" style="left:8px;top:35px;width:22px;height:3.5px;background:var(--orange)"></div>
  <div class="abs" style="left:35px;top:35px;width:22px;height:3.5px;background:var(--dark)"></div>
  <div class="abs" style="left:62px;top:35px;width:22px;height:3.5px;background:var(--dark)"></div>
  <div class="abs" style="left:89px;top:35px;width:22px;height:3.5px;background:var(--orange)"></div>
  <p class="p c" style="left:8px;width:22px;top:16px;height:4px"><span class="h w">Title</span></p>
  <p class="p c" style="left:35px;width:22px;top:16px;height:4px"><span class="h w">Title</span></p>
  <p class="p c" style="left:62px;width:22px;top:16px;height:4px"><span class="h w">Title</span></p>
  <p class="p c" style="left:89px;width:22px;top:16px;height:4px"><span class="h w">Title</span></p>
  <p class="p c" style="left:8px;width:22px;top:35px;height:4px"><span class="h w">Title</span></p>
  <p class="p c" style="left:35px;width:22px;top:35px;height:4px"><span class="h w">Title</span></p>
  <p class="p c" style="left:62px;width:22px;top:35px;height:4px"><span class="h w">Title</span></p>
  <p class="p c" style="left:89px;width:22px;top:35px;height:4px"><span class="h w">Title</span></p>
  <p class="p c" style="left:8px;width:22px;top:21px;height:9px">Short text about this point goes here in a few words.</p>
  <p class="p c" style="left:35px;width:22px;top:21px;height:9px">Short text about this point goes here in a few words.</p>
  <p class="p c" style="left:62px;width:22px;top:21px;height:9px">Short text about this point goes here in a few words.</p>
  <p class="p c" style="left:89px;width:22px;top:21px;height:9px">Short text about this point goes here in a few words.</p>
  <p class="p c" style="left:8px;width:22px;top:40px;height:9px">Short text about this point goes here in a few words.</p>
  <p class="p c" style="left:35px;width:22px;top:40px;height:9px">Short text about this point goes here in a few words.</p>
  <p class="p c" style="left:62px;width:22px;top:40px;height:9px">Short text about this point goes here in a few words.</p>
  <p class="p c" style="left:89px;width:22px;top:40px;height:9px">Short text about this point goes here in a few words.</p>
  <div class="foot"></div>
</div><div class="caption"><span class="num">12</span><span class="meta">★</span></div></div>

<!-- 13 -->
<div class="cell"><div class="slide">
  <div class="title">TITLE HERE</div><div class="brand">NEXORA</div><div class="topline"></div>
  <div class="abs" style="left:16px;right:16px;top:23px;height:.5px;background:#bbb"></div>
  <svg class="ico" style="left:20px;top:19px" width="8" height="8" viewBox="0 0 10 10" aria-hidden="true"><circle cx="5" cy="5" r="5" fill="var(--orange)"/><path d="M3 5.2 4.5 6.6 7.2 3.6" fill="none" stroke="#fff" stroke-width="1"/></svg>
  <svg class="ico" style="left:43px;top:19px" width="8" height="8" viewBox="0 0 10 10" aria-hidden="true"><circle cx="5" cy="5" r="5" fill="var(--dark)"/><path d="M5 2.5V5l1.8 1.2" fill="none" stroke="#fff" stroke-width="1"/></svg>
  <svg class="ico" style="left:66px;top:19px" width="8" height="8" viewBox="0 0 10 10" aria-hidden="true"><circle cx="5" cy="5" r="5" fill="var(--dark)"/><path d="M5 2.3c-1.3 0-2.2 1-2.2 2.2C2.8 6 5 7.8 5 7.8S7.2 6 7.2 4.5c0-1.2-.9-2.2-2.2-2.2z" fill="#fff"/></svg>
  <svg class="ico" style="left:89px;top:19px" width="8" height="8" viewBox="0 0 10 10" aria-hidden="true"><circle cx="5" cy="5" r="5" fill="var(--dark)"/><path d="M3 6.8h4M3.5 6.8V5M5 6.8V3.4M6.5 6.8V4.4" fill="none" stroke="#fff" stroke-width=".9"/></svg>
  <p class="p c" style="left:13px;width:22px;top:29px;height:14px"><span class="h o">Title</span>Short text about this point goes here in a few words.</p>
  <p class="p c" style="left:36px;width:22px;top:29px;height:14px"><span class="h">Title</span>Short text about this point goes here in a few words.</p>
  <p class="p c" style="left:59px;width:22px;top:29px;height:14px"><span class="h">Title</span>Short text about this point goes here in a few words.</p>
  <p class="p c" style="left:82px;width:22px;top:29px;height:14px"><span class="h">Title</span>Short text about this point goes here in a few words.</p>
  <div class="foot"></div>
</div><div class="caption"><span class="num">13</span><span class="meta">★</span></div></div>

<!-- 14 -->
<div class="cell"><div class="slide">
  <div class="title">Our Best Features</div><div class="brand">NEXORA</div>
  <div class="abs" style="left:0;width:39px;top:27px;height:31px;background:var(--orange)"></div>
  <div class="abs" style="left:39px;width:40px;top:27px;height:31px;background:#a8a8a8"></div>
  <div class="abs" style="left:79px;right:0;top:27px;height:31px;background:#cfcfcf"></div>
  <svg class="ico" style="left:17px;top:31px" width="5" height="5" viewBox="0 0 10 10" aria-hidden="true"><path d="M2 8 7.5 2.5M6 1.5l2.5 2.5" fill="none" stroke="#fff" stroke-width="1.2"/></svg>
  <svg class="ico" style="left:57px;top:31px" width="5" height="5" viewBox="0 0 10 10" aria-hidden="true"><rect x="1" y="2" width="8" height="5.5" fill="none" stroke="#fff" stroke-width="1"/><path d="M3.5 9h3" stroke="#fff" stroke-width="1"/></svg>
  <svg class="ico" style="left:97px;top:31px" width="5" height="5" viewBox="0 0 10 10" aria-hidden="true"><path d="M5 1 9 8.5H1Z" fill="none" stroke="#fff" stroke-width="1"/></svg>
  <p class="p w c" style="left:6px;width:27px;top:38px;height:13px"><span class="h w">Feature</span>Short text about this point goes here in a few words.</p>
  <p class="p w c" style="left:46px;width:27px;top:38px;height:13px"><span class="h w">Feature</span>Short text about this point goes here in a few words.</p>
  <p class="p w c" style="left:86px;width:27px;top:38px;height:13px"><span class="h w">Feature</span>Short text about this point goes here in a few words.</p>
</div><div class="caption"><span class="num">14</span><span class="meta">★</span></div></div>

<!-- 15 -->
<div class="cell"><div class="slide">
  <div class="title">Our Main Service</div><div class="brand">NEXORA</div>
  <p class="p" style="left:6px;width:28px;top:12px;height:12px"><span class="h">Service</span>Short text about this point goes here in a few words.</p>
  <p class="p" style="left:44px;width:28px;top:12px;height:12px"><span class="h">Service</span>Short text about this point goes here in a few words.</p>
  <p class="p" style="left:82px;width:28px;top:12px;height:12px"><span class="h">Service</span>Short text about this point goes here in a few words.</p>
  <p class="p" style="left:6px;width:28px;top:27px;height:12px"><span class="h">Service</span>Short text about this point goes here in a few words.</p>
  <p class="p" style="left:44px;width:28px;top:27px;height:12px"><span class="h">Service</span>Short text about this point goes here in a few words.</p>
  <p class="p" style="left:82px;width:28px;top:27px;height:12px"><span class="h">Service</span>Short text about this point goes here in a few words.</p>
  <p class="p" style="left:6px;width:28px;top:42px;height:12px"><span class="h">Service</span>Short text about this point goes here in a few words.</p>
  <p class="p" style="left:44px;width:28px;top:42px;height:12px"><span class="h">Service</span>Short text about this point goes here in a few words.</p>
  <p class="p" style="left:82px;width:28px;top:42px;height:12px"><span class="h">Service</span>Short text about this point goes here in a few words.</p>
  <div class="foot"></div>
</div><div class="caption"><span class="num">15</span><span class="meta">★</span></div></div>

<!-- 16 -->
<div class="cell"><div class="slide">
  <div class="abs" style="left:22px;top:6px;width:18px;height:18px;background:#eee"></div>
  <div class="abs" style="left:44px;top:4px;width:22px;height:20px;background:#eee"></div>
  <div class="abs" style="left:70px;top:6px;width:18px;height:18px;background:#eee"></div>
  <div class="abs" style="left:92px;top:6px;width:20px;height:18px;background:#eee"></div>
  <div class="abs" style="left:70px;top:28px;width:18px;height:14px;background:#eee"></div>
  <div class="abs" style="left:92px;top:28px;width:20px;height:14px;background:#eee"></div>
  <div class="abs" style="left:44px;top:46px;width:22px;height:15px;background:#eee"></div>
  <div class="abs" style="left:70px;top:46px;width:42px;height:15px;background:#eee"></div>
  <div class="abs" style="left:0;top:27px;width:66px;height:16px;background:var(--orange)"></div>
  <div class="hero-text" style="left:14px;top:30px;font-size:4.6px;font-weight:700">Project Portfolio</div>
  <p class="p w" style="left:20px;width:30px;top:37px;height:3px">Your text here</p>
  <div class="circ" style="right:4px;bottom:3px;width:4px;height:4px;background:#222"></div>
</div><div class="caption"><span class="num">16</span><span class="meta">★</span></div></div>

<!-- 17 -->
<div class="cell"><div class="slide">
  <div class="abs" style="inset:0;background:linear-gradient(90deg,var(--orange-deep) 0%,var(--orange) 40%,#c69b70 100%)" role="img" aria-label="Orange toned photo of a hand touching digital service icons"></div>
  <div class="hero-text" style="left:12px;top:24px;font-size:6.5px;line-height:1.35">OUR<br>Services</div>
  <div class="brand light" style="top:9px;right:20px;font-size:4.5px">NEXORA</div>
</div><div class="caption"><span class="num">17</span></div></div>

<!-- 18 -->
<div class="cell"><div class="slide">
  <div class="abs photo-net" style="left:0;width:58px;top:12px;bottom:0" role="img" aria-label="Photo of a hand touching a network graphic"></div>
  <div class="title">TEXT HERE</div><div class="brand">NEXORA</div>
  <div class="sq" style="left:63px;top:17px;width:4px;height:4px"></div>
  <div class="sq" style="left:63px;top:25px;width:4px;height:4px"></div>
  <div class="sq" style="left:63px;top:33px;width:4px;height:4px"></div>
  <div class="sq" style="left:63px;top:41px;width:4px;height:4px"></div>
  <div class="sq" style="left:63px;top:49px;width:4px;height:4px"></div>
  <p class="p" style="left:70px;right:6px;top:16.5px;height:6px">Short text about this point goes here in a few words.</p>
  <p class="p" style="left:70px;right:6px;top:24.5px;height:6px">Short text about this point goes here in a few words.</p>
  <p class="p" style="left:70px;right:6px;top:32.5px;height:6px">Short text about this point goes here in a few words.</p>
  <p class="p" style="left:70px;right:6px;top:40.5px;height:6px">Short text about this point goes here in a few words.</p>
  <p class="p" style="left:70px;right:6px;top:48.5px;height:6px">Short text about this point goes here in a few words.</p>
</div><div class="caption"><span class="num">18</span><span class="meta">★</span></div></div>

<!-- 19 -->
<div class="cell"><div class="slide">
  <div class="title">Investment Rotation</div><div class="brand">NEXORA</div>
  <svg class="abs" style="left:40px;top:16px" width="38" height="38" viewBox="0 0 38 38" aria-hidden="true">
    <circle cx="19" cy="19" r="13" fill="none" stroke="var(--orange)" stroke-width="8" stroke-dasharray="20 0.8"/>
    <circle cx="19" cy="19" r="13" fill="none" stroke="var(--dark)" stroke-width="8" stroke-dasharray="20 61" stroke-dashoffset="-20"/>
    <circle cx="19" cy="19" r="13" fill="none" stroke="#888" stroke-width="8" stroke-dasharray="18 63" stroke-dashoffset="-60"/>
  </svg>
  <p class="p" style="left:12px;width:24px;top:23px;height:9px;text-align:right"><span class="h">Title</span>Short text about this point goes here in a few words.</p>
  <p class="p" style="left:82px;width:24px;top:26px;height:9px"><span class="h">Title</span>Short text about this point goes here in a few words.</p>
  <p class="p" style="left:82px;width:24px;top:44px;height:9px"><span class="h o">Title</span>Short text about this point goes here in a few words.</p>
  <div class="foot"></div>
</div><div class="caption"><span class="num">19</span><span class="meta">★</span></div></div>

<!-- 20 -->
<div class="cell"><div class="slide">
  <div class="title">Infographic Layout</div><div class="brand">NEXORA</div>
  <div class="abs" style="left:8px;right:10px;top:17px;height:.6px;background:var(--dark)"></div>
  <p class="p" style="left:30px;width:12px;top:12px;height:4px"><span class="h">Step</span></p>
  <p class="p" style="left:50px;width:12px;top:12px;height:4px"><span class="h">Step</span></p>
  <p class="p" style="left:70px;width:12px;top:12px;height:4px"><span class="h">Step</span></p>
  <p class="p" style="left:90px;width:12px;top:12px;height:4px"><span class="h">Step</span></p>
  <svg class="ico" style="left:6px;top:24px" width="4.5" height="4.5" viewBox="0 0 10 10" aria-hidden="true"><circle cx="5" cy="5" r="5" fill="var(--green)"/><path d="M2.8 5.2 4.4 6.8 7.4 3.6" fill="none" stroke="#fff" stroke-width="1.3"/></svg>
  <svg class="ico" style="left:6px;top:34px" width="4.5" height="4.5" viewBox="0 0 10 10" aria-hidden="true"><circle cx="5" cy="5" r="5" fill="var(--orange)"/><path d="M2.8 5.2 4.4 6.8 7.4 3.6" fill="none" stroke="#fff" stroke-width="1.3"/></svg>
  <svg class="ico" style="left:6px;top:44px" width="4.5" height="4.5" viewBox="0 0 10 10" aria-hidden="true"><circle cx="5" cy="5" r="5" fill="var(--green)"/><path d="M2.8 5.2 4.4 6.8 7.4 3.6" fill="none" stroke="#fff" stroke-width="1.3"/></svg>
  <svg class="ico" style="left:56px;top:24px" width="4.5" height="4.5" viewBox="0 0 10 10" aria-hidden="true"><circle cx="5" cy="5" r="5" fill="var(--green)"/><path d="M2.8 5.2 4.4 6.8 7.4 3.6" fill="none" stroke="#fff" stroke-width="1.3"/></svg>
  <svg class="ico" style="left:56px;top:34px" width="4.5" height="4.5" viewBox="0 0 10 10" aria-hidden="true"><circle cx="5" cy="5" r="5" fill="var(--orange)"/><path d="M2.8 5.2 4.4 6.8 7.4 3.6" fill="none" stroke="#fff" stroke-width="1.3"/></svg>
  <svg class="ico" style="left:56px;top:44px" width="4.5" height="4.5" viewBox="0 0 10 10" aria-hidden="true"><circle cx="5" cy="5" r="5" fill="var(--green)"/><path d="M2.8 5.2 4.4 6.8 7.4 3.6" fill="none" stroke="#fff" stroke-width="1.3"/></svg>
  <p class="p" style="left:13px;width:36px;top:22.5px;height:9px"><span class="h">Title</span>Short text about this point goes here in a few words.</p>
  <p class="p" style="left:13px;width:36px;top:32.5px;height:9px"><span class="h">Title</span>Short text about this point goes here in a few words.</p>
  <p class="p" style="left:13px;width:36px;top:42.5px;height:9px"><span class="h">Title</span>Short text about this point goes here in a few words.</p>
  <p class="p" style="left:63px;width:36px;top:22.5px;height:9px"><span class="h">Title</span>Short text about this point goes here in a few words.</p>
  <p class="p" style="left:63px;width:36px;top:32.5px;height:9px"><span class="h">Title</span>Short text about this point goes here in a few words.</p>
  <p class="p" style="left:63px;width:36px;top:42.5px;height:9px"><span class="h">Title</span>Short text about this point goes here in a few words.</p>
  <div class="foot"></div>
</div><div class="caption"><span class="num">20</span><span class="meta">★</span></div></div>

<!-- 21 -->
<div class="cell"><div class="slide">
  <div class="title">Business Layout</div><div class="brand">NEXORA</div>
  <div class="abs" style="left:18px;top:13px;width:19px;height:28px;background:var(--orange)"></div>
  <div class="abs" style="left:39px;top:13px;width:19px;height:28px;background:var(--dark)"></div>
  <div class="abs" style="left:60px;top:13px;width:19px;height:28px;background:var(--orange)"></div>
  <div class="abs" style="left:81px;top:13px;width:19px;height:28px;background:#9a9a9a"></div>
  <svg class="ico" style="left:24px;top:16px" width="7" height="7" viewBox="0 0 10 10" aria-hidden="true"><rect x="1" y="3" width="8" height="5.5" rx="1" fill="#fff"/><rect x="3.5" y="1.8" width="3" height="1.5" fill="#fff"/><circle cx="5" cy="5.7" r="1.6" fill="var(--orange)"/></svg>
  <svg class="ico" style="left:45px;top:16px" width="7" height="7" viewBox="0 0 10 10" aria-hidden="true"><path d="M8 4A3.2 3.2 0 0 0 2.3 3.2M2 6a3.2 3.2 0 0 0 5.7.8" fill="none" stroke="#fff" stroke-width="1.1"/><path d="M2 1.5v2.2h2.2M8 8.5V6.3H5.8" fill="none" stroke="#fff" stroke-width="1"/></svg>
  <svg class="ico" style="left:66px;top:16px" width="7" height="7" viewBox="0 0 10 10" aria-hidden="true"><path d="M2 8 7.5 2.5M6 1.5l2.5 2.5" fill="none" stroke="#fff" stroke-width="1.3"/></svg>
  <svg class="ico" style="left:87px;top:16px" width="7" height="7" viewBox="0 0 10 10" aria-hidden="true"><path d="M5 1 9 8.5H1Z" fill="#fff"/></svg>
  <p class="p w c" style="left:18px;width:19px;top:25px;height:14px"><span class="h w">Label</span>Short text about this point.</p>
  <p class="p w c" style="left:39px;width:19px;top:25px;height:14px"><span class="h w">Label</span>Short text about this point.</p>
  <p class="p w c" style="left:60px;width:19px;top:25px;height:14px"><span class="h w">Label</span>Short text about this point.</p>
  <p class="p w c" style="left:81px;width:19px;top:25px;height:14px"><span class="h w">Label</span>Short text about this point.</p>
  <div class="abs" style="left:18px;right:18px;top:44px;height:.5px;background:#bbb"></div>
  <p class="p" style="left:12px;width:45px;top:47px;height:10px">Short text about this point goes here in a few words. Short text about this point goes here in a few words.</p>
  <p class="p" style="left:62px;width:45px;top:47px;height:10px">Short text about this point goes here in a few words. Short text about this point goes here in a few words.</p>
  <div class="foot"></div>
</div><div class="caption"><span class="num">21</span><span class="meta">★</span></div></div>

<!-- 22 -->
<div class="cell"><div class="slide selected">
  <div class="title">Title here</div><div class="brand">NEXORA</div>
  <p class="p" style="left:5px;right:8px;top:10px;height:7px"><span class="h o">Chart Summary</span>Our team designs, builds and supports secure information systems for growing businesses. We combine cloud services, smart networks and clear advice so every client can work faster, protect its data and plan the next step with confidence and care.</p>
  <div class="abs" style="left:5px;top:18px;width:50px;height:32px;background:#9d9d9d"></div>
  <p class="p" style="left:60px;right:6px;top:18px;height:6px">Short text about this point goes here in a few words.</p>
  <svg class="abs" style="left:64px;top:26px" width="46" height="20" viewBox="0 0 46 20" aria-hidden="true">
    <circle cx="9" cy="9" r="8" fill="#bcbcbc"/><path d="M9 9 L9 1 A8 8 0 0 1 16.5 11 Z" fill="var(--dark)"/>
    <circle cx="35" cy="9" r="8" fill="#bcbcbc"/><path d="M35 9 L35 1 A8 8 0 0 1 40 15 Z" fill="var(--dark)"/>
  </svg>
  <div class="foot"></div>
</div><div class="caption selected"><span class="num">22</span><span class="meta">★</span></div></div>

<!-- 23 -->
<div class="cell"><div class="slide">
  <div class="abs photo-net-grey" style="inset:0" role="img" aria-label="Greyscale photo of a hand touching a network graphic"></div>
  <div class="abs" style="left:0;right:0;top:27px;height:24px;background:rgba(247,144,30,.9)"></div>
  <div class="hero-text" style="left:10px;top:31px;font-size:7px">TITLE PAGE</div>
  <div class="hero-text" style="left:10px;top:40px;font-size:3px;font-weight:400">YOUR TEXT IS HERE</div>
  <div class="brand big light" style="top:35px;right:14px">NEXORA</div>
</div><div class="caption"><span class="num">23</span></div></div>

<!-- 24 -->
<div class="cell"><div class="slide">
  <div class="title">Infographic Layout</div><div class="brand">NEXORA</div>
  <svg class="abs" style="left:40px;top:14px" width="38" height="38" viewBox="0 0 38 38" aria-hidden="true">
    <circle cx="19" cy="19" r="13" fill="none" stroke="#5c5c5c" stroke-width="6" stroke-dasharray="12 2"/>
    <circle cx="19" cy="19" r="13" fill="none" stroke="var(--orange)" stroke-width="6" stroke-dasharray="12 70" stroke-dashoffset="-28"/>
    <circle cx="19" cy="19" r="13" fill="none" stroke="var(--orange)" stroke-width="6" stroke-dasharray="12 70" stroke-dashoffset="-56"/>
  </svg>
  <p class="p" style="left:8px;width:28px;top:16px;height:9px;text-align:right"><span class="h">Title</span>Short text about this point goes here in a few words.</p>
  <p class="p" style="left:8px;width:28px;top:27px;height:9px;text-align:right"><span class="h">Title</span>Short text about this point goes here in a few words.</p>
  <p class="p" style="left:8px;width:28px;top:38px;height:9px;text-align:right"><span class="h o">Title</span>Short text about this point goes here in a few words.</p>
  <p class="p" style="left:82px;width:28px;top:16px;height:9px"><span class="h">Title</span>Short text about this point goes here in a few words.</p>
  <p class="p" style="left:82px;width:28px;top:27px;height:9px"><span class="h">Title</span>Short text about this point goes here in a few words.</p>
  <p class="p" style="left:82px;width:28px;top:38px;height:9px"><span class="h">Title</span>Short text about this point goes here in a few words.</p>
  <div class="foot"></div>
</div><div class="caption"><span class="num">24</span><span class="meta">★</span></div></div>

<!-- 25 -->
<div class="cell"><div class="slide">
  <div class="title" style="top:8px">CIRCLE INFOGRAPHICS</div><div class="brand">NEXORA</div>
  <p class="p" style="left:5px;width:40px;top:15px;height:8px"><span class="h">Subtitle</span>Short text about this point goes here in a few words.</p>
  <div class="sq" style="left:6px;top:28px;width:4px;height:4px"></div>
  <div class="sq" style="left:6px;top:36px;width:4px;height:4px;background:var(--dark)"></div>
  <div class="sq" style="left:6px;top:44px;width:4px;height:4px"></div>
  <p class="p" style="left:13px;width:28px;top:27.5px;height:6px">Short text about this point goes here in a few words.</p>
  <p class="p" style="left:13px;width:28px;top:35.5px;height:6px">Short text about this point goes here in a few words.</p>
  <p class="p" style="left:13px;width:28px;top:43.5px;height:6px">Short text about this point goes here in a few words.</p>
  <svg class="abs" style="left:54px;top:24px" width="28" height="28" viewBox="0 0 28 28" aria-hidden="true">
    <circle cx="14" cy="14" r="10" fill="none" stroke="var(--orange)" stroke-width="5" stroke-dasharray="40 23"/>
    <circle cx="14" cy="14" r="10" fill="none" stroke="var(--dark)" stroke-width="5" stroke-dasharray="23 40" stroke-dashoffset="-40"/>
  </svg>
  <p class="p" style="left:86px;width:26px;top:27.5px;height:6px">Short text about this point goes here in a few words.</p>
  <p class="p" style="left:86px;width:26px;top:35.5px;height:6px">Short text about this point goes here in a few words.</p>
  <p class="p" style="left:86px;width:26px;top:43.5px;height:6px">Short text about this point goes here in a few words.</p>
  <div class="foot"></div>
</div><div class="caption"><span class="num">25</span><span class="meta">★ 00:00</span></div></div>

<!-- 26 -->
<div class="cell"><div class="slide">
  <div class="title" style="line-height:1.2">CUSTOM<br>INFOGRAPHIC</div><div class="brand">NEXORA</div>
  <div class="abs" style="left:47px;top:17px;width:10px;height:10px;background:var(--orange)"></div>
  <div class="abs" style="left:61px;top:17px;width:10px;height:10px;background:var(--dark)"></div>
  <div class="abs" style="left:47px;top:31px;width:10px;height:10px;background:var(--dark)"></div>
  <div class="abs" style="left:61px;top:31px;width:10px;height:10px;background:var(--orange)"></div>
  <svg class="ico" style="left:49.5px;top:19.5px" width="5" height="5" viewBox="0 0 10 10" aria-hidden="true"><path d="M5 1 9 8.5H1Z" fill="#fff"/></svg>
  <svg class="ico" style="left:63.5px;top:19.5px" width="5" height="5" viewBox="0 0 10 10" aria-hidden="true"><rect x="1" y="1" width="8" height="8" fill="none" stroke="#fff" stroke-width="1.2"/><path d="M1 5h8M5 1v8" stroke="#fff" stroke-width="1"/></svg>
  <svg class="ico" style="left:49.5px;top:33.5px" width="5" height="5" viewBox="0 0 10 10" aria-hidden="true"><rect x="1" y="3" width="8" height="6" fill="#fff"/><rect x="3.5" y="1" width="3" height="2" fill="none" stroke="#fff" stroke-width="1"/></svg>
  <svg class="ico" style="left:63.5px;top:33.5px" width="5" height="5" viewBox="0 0 10 10" aria-hidden="true"><path d="M2 8 7.5 2.5M6 1.5l2.5 2.5" fill="none" stroke="#fff" stroke-width="1.4"/></svg>
  <p class="p" style="left:12px;width:30px;top:16.5px;height:10px;text-align:right"><span class="h">Title</span>Short text about this point goes here in a few words.</p>
  <p class="p" style="left:12px;width:30px;top:30.5px;height:10px;text-align:right"><span class="h">Title</span>Short text about this point goes here in a few words.</p>
  <p class="p" style="left:76px;width:30px;top:16.5px;height:10px"><span class="h">Title</span>Short text about this point goes here in a few words.</p>
  <p class="p" style="left:76px;width:30px;top:30.5px;height:10px"><span class="h">Title</span>Short text about this point goes here in a few words.</p>
  <div class="foot"></div>
</div><div class="caption"><span class="num">26</span><span class="meta">★ 00:04</span></div></div>

<!-- 27 -->
<div class="cell"><div class="slide">
  <div class="title">CAR APPLICATION</div>
  <div class="circ" style="left:8px;top:19px;width:8px;height:8px;border:.7px solid #888"></div>
  <div class="circ" style="left:8px;top:31px;width:8px;height:8px;border:.7px solid #888"></div>
  <div class="circ" style="left:8px;top:43px;width:8px;height:8px;border:.7px solid #888"></div>
  <p class="p" style="left:19px;width:48px;top:19.5px;height:7px">Short text about this point goes here in a few words.</p>
  <p class="p" style="left:19px;width:48px;top:31.5px;height:7px">Short text about this point goes here in a few words.</p>
  <p class="p" style="left:19px;width:48px;top:43.5px;height:7px">Short text about this point goes here in a few words.</p>
  <div class="abs photo-phone" style="left:72px;right:6px;top:8px;bottom:0" role="img" aria-label="Photo of a hand holding a smartphone"></div>
  <div class="abs" style="left:79px;top:10px;width:18px;height:34px;border-radius:3px;background:#fff;border:1.5px solid #222"></div>
</div><div class="caption"><span class="num">27</span><span class="meta">★</span></div></div>

<!-- 28 -->
<div class="cell"><div class="slide">
  <div class="title" style="line-height:1.2">CUSTOM<br>INFOGRAPHIC</div><div class="brand">NEXORA</div>
  <svg class="abs" style="left:42px;top:16px" width="34" height="34" viewBox="0 0 34 34" aria-hidden="true">
    <circle cx="17" cy="17" r="13" fill="none" stroke="#cfcfcf" stroke-width="2.5"/>
    <circle cx="17" cy="17" r="13" fill="none" stroke="var(--orange)" stroke-width="2.5" stroke-dasharray="30 52"/>
    <circle cx="17" cy="17" r="7" fill="var(--dark)"/>
    <rect x="13.5" y="15" width="7" height="5" fill="#fff"/><rect x="15.5" y="13.5" width="3" height="1.5" fill="none" stroke="#fff" stroke-width=".7"/>
  </svg>
  <div class="sq" style="left:6px;top:24px;width:4px;height:4px"></div>
  <div class="sq" style="left:6px;top:38px;width:4px;height:4px"></div>
  <p class="p" style="left:12px;width:28px;top:23.5px;height:10px"><span class="h">Title</span>Short text about this point goes here in a few words.</p>
  <p class="p" style="left:12px;width:28px;top:37.5px;height:10px"><span class="h">Title</span>Short text about this point goes here in a few words.</p>
  <p class="p" style="left:80px;width:30px;top:23.5px;height:10px"><span class="h">Title</span>Short text about this point goes here in a few words.</p>
  <p class="p" style="left:80px;width:30px;top:37.5px;height:10px"><span class="h">Title</span>Short text about this point goes here in a few words.</p>
  <div class="foot"></div>
</div><div class="caption"><span class="num">28</span><span class="meta">★ 00:04</span></div></div>

<!-- 29 -->
<div class="cell"><div class="slide">
  <div class="abs" style="left:0;width:58px;top:0;bottom:0;background:var(--orange)"></div>
  <div class="abs photo-office" style="left:58px;right:0;top:0;bottom:0" role="img" aria-label="Photo of a person writing at a desk"></div>
  <div class="hero-text" style="left:16px;top:24px;font-size:6.5px;line-height:1.35">Tilte<br>Here</div>
  <div class="brand light" style="top:6px;right:auto;left:48px;font-size:4.5px">NEXORA</div>
</div><div class="caption"><span class="num">29</span></div></div>

<!-- 30 -->
<div class="cell"><div class="slide">
  <div class="title">graph</div><div class="brand">NEXORA</div>
  <p class="p c" style="left:8px;width:44px;top:15px;height:3px"><span class="h">Sales Report</span></p>
  <p class="p c" style="left:64px;width:44px;top:15px;height:3px"><span class="h">Growth Rate</span></p>
  <svg class="abs" style="left:6px;top:18px" width="106" height="40" viewBox="0 0 106 40" aria-hidden="true">
    <g fill="var(--orange)"><rect x="4" y="18" width="2.5" height="16"/><rect x="12" y="12" width="2.5" height="22"/><rect x="20" y="20" width="2.5" height="14"/><rect x="28" y="10" width="2.5" height="24"/><rect x="36" y="16" width="2.5" height="18"/></g>
    <g fill="var(--dark)"><rect x="7" y="22" width="2.5" height="12"/><rect x="15" y="17" width="2.5" height="17"/><rect x="23" y="24" width="2.5" height="10"/><rect x="31" y="15" width="2.5" height="19"/><rect x="39" y="21" width="2.5" height="13"/></g>
    <line x1="2" y1="34" x2="46" y2="34" stroke="#bbb" stroke-width=".5"/>
    <line x1="58" y1="34" x2="102" y2="34" stroke="#bbb" stroke-width=".5"/>
    <polyline points="60,22 70,18 80,20 90,14 100,16" fill="none" stroke="var(--orange)" stroke-width=".9"/>
    <polyline points="60,26 70,24 80,28 90,22 100,26" fill="none" stroke="var(--dark)" stroke-width=".9"/>
    <polyline points="60,30 70,28 80,25 90,27 100,23" fill="none" stroke="#aaa" stroke-width=".9"/>
  </svg>
  <div class="foot"></div>
</div><div class="caption"><span class="num">30</span></div></div>

<!-- 31 -->
<div class="cell"><div class="slide">
  <div class="title">graph</div><div class="brand">NEXORA</div>
  <p class="p c" style="left:20px;width:20px;top:12px;height:3px"><span class="h">Share</span></p>
  <p class="p c" style="left:70px;width:20px;top:12px;height:3px"><span class="h">Market</span></p>
  <svg class="abs" style="left:10px;top:16px" width="100" height="42" viewBox="0 0 100 42" aria-hidden="true">
    <circle cx="20" cy="20" r="11" fill="none" stroke="var(--orange)" stroke-width="6" stroke-dasharray="30 40"/>
    <circle cx="20" cy="20" r="11" fill="none" stroke="var(--dark)" stroke-width="6" stroke-dasharray="22 48" stroke-dashoffset="-30"/>
    <circle cx="20" cy="20" r="11" fill="none" stroke="#bbb" stroke-width="6" stroke-dasharray="17 53" stroke-dashoffset="-52"/>
    <circle cx="70" cy="20" r="15" fill="#777"/>
    <path d="M70 20 L70 5 A15 15 0 0 1 84 25 Z" fill="var(--orange)"/>
    <path d="M70 20 L84 25 A15 15 0 0 1 62 33 Z" fill="var(--dark)"/>
  </svg>
  <div class="foot"></div>
</div><div class="caption"><span class="num">31</span></div></div>

<!-- 32 -->
<div class="cell"><div class="slide">
  <div class="title">GRAPH</div><div class="brand">NEXORA</div>
  <p class="p" style="left:8px;width:28px;top:22px;height:10px"><span class="h o">Label</span>Short text about this point goes here in a few words.</p>
  <svg class="abs" style="left:40px;top:14px" width="60" height="40" viewBox="0 0 60 40" aria-hidden="true">
    <ellipse cx="30" cy="24" rx="24" ry="11" fill="#3e3e3e"/>
    <ellipse cx="30" cy="21" rx="24" ry="11" fill="#6a6a6a"/>
    <path d="M30 21 L30 10 A24 11 0 0 1 54 21 Z" fill="var(--orange)"/>
    <path d="M30 21 L54 21 A24 11 0 0 1 36 31.8 Z" fill="#8c8c8c"/>
    <line x1="44" y1="12" x2="54" y2="3" stroke="var(--orange)" stroke-width=".6"/>
  </svg>
  <p class="p" style="left:95px;width:18px;top:12px;height:10px"><span class="h o">Label</span>Short text about this point goes here in a few words.</p>
  <div class="foot"></div>
</div><div class="caption"><span class="num">32</span><span class="meta">★ 00:00</span></div></div>

<!-- 33 -->
<div class="cell"><div class="slide">
  <div class="title">Table page</div><div class="brand">NEXORA</div>
  <svg class="abs" style="left:6px;top:14px" width="106" height="44" viewBox="0 0 106 44" font-family="Open Sans, sans-serif" font-size="1.9" text-anchor="middle" aria-hidden="true">
    <rect width="106" height="4" fill="var(--orange)"/>
    <rect y="4" width="14" height="40" fill="var(--dark)"/>
    <g fill="#eee"><rect x="14" y="4" width="92" height="5"/><rect x="14" y="14" width="92" height="5"/><rect x="14" y="24" width="92" height="5"/><rect x="14" y="34" width="92" height="5"/></g>
    <g fill="#dcdcdc"><rect x="14" y="9" width="92" height="5"/><rect x="14" y="19" width="92" height="5"/><rect x="14" y="29" width="92" height="5"/><rect x="14" y="39" width="92" height="5"/></g>
    <g fill="#fff"><text x="7" y="2.8">Item</text><text x="20" y="2.8">Data</text><text x="32" y="2.8">Data</text><text x="44" y="2.8">Data</text><text x="56" y="2.8">Data</text><text x="68" y="2.8">Data</text><text x="80" y="2.8">Data</text><text x="94" y="2.8">Data</text></g>
    <g fill="#fff"><text x="7" y="7.3">Item</text><text x="7" y="12.3">Item</text><text x="7" y="17.3">Item</text><text x="7" y="22.3">Item</text><text x="7" y="27.3">Item</text><text x="7" y="32.3">Item</text><text x="7" y="37.3">Item</text></g>
    <g fill="#777">
      <text x="20" y="7.3">Data</text><text x="32" y="7.3">Data</text><text x="44" y="7.3">Data</text><text x="56" y="7.3">Data</text><text x="68" y="7.3">Data</text><text x="80" y="7.3">Data</text><text x="94" y="7.3">Data</text>
      <text x="20" y="12.3">Data</text><text x="32" y="12.3">Data</text><text x="44" y="12.3">Data</text><text x="56" y="12.3">Data</text><text x="68" y="12.3">Data</text><text x="80" y="12.3">Data</text><text x="94" y="12.3">Data</text>
      <text x="20" y="17.3">Data</text><text x="32" y="17.3">Data</text><text x="44" y="17.3">Data</text><text x="56" y="17.3">Data</text><text x="68" y="17.3">Data</text><text x="80" y="17.3">Data</text><text x="94" y="17.3">Data</text>
      <text x="20" y="22.3">Data</text><text x="32" y="22.3">Data</text><text x="44" y="22.3">Data</text><text x="56" y="22.3">Data</text><text x="68" y="22.3">Data</text><text x="80" y="22.3">Data</text><text x="94" y="22.3">Data</text>
      <text x="20" y="27.3">Data</text><text x="32" y="27.3">Data</text><text x="44" y="27.3">Data</text><text x="56" y="27.3">Data</text><text x="68" y="27.3">Data</text><text x="80" y="27.3">Data</text><text x="94" y="27.3">Data</text>
      <text x="20" y="32.3">Data</text><text x="32" y="32.3">Data</text><text x="44" y="32.3">Data</text><text x="56" y="32.3">Data</text><text x="68" y="32.3">Data</text><text x="80" y="32.3">Data</text><text x="94" y="32.3">Data</text>
      <text x="20" y="37.3">Data</text><text x="32" y="37.3">Data</text><text x="44" y="37.3">Data</text><text x="56" y="37.3">Data</text><text x="68" y="37.3">Data</text><text x="80" y="37.3">Data</text><text x="94" y="37.3">Data</text>
    </g>
  </svg>
  <div class="abs" style="right:3px;bottom:2px;width:5px;height:5px;background:#111"></div>
</div><div class="caption"><span class="num">33</span></div></div>

<!-- 34 -->
<div class="cell"><div class="slide">
  <div class="title">Price Table</div>
  <div class="abs" style="left:8px;top:14px;width:22px;height:12px;background:var(--orange)"></div>
  <div class="abs" style="left:34px;top:14px;width:22px;height:12px;background:#888"></div>
  <div class="abs" style="left:60px;top:14px;width:22px;height:12px;background:#333d48"></div>
  <div class="abs" style="left:86px;top:14px;width:22px;height:12px;background:var(--orange)"></div>
  <div class="hero-text" style="left:12px;top:16px;font-size:6px">120$</div>
  <div class="hero-text" style="left:38px;top:16px;font-size:6px">140$</div>
  <div class="hero-text" style="left:64px;top:16px;font-size:6px">170$</div>
  <div class="hero-text" style="left:90px;top:16px;font-size:6px">190$</div>
  <p class="p c" style="left:8px;width:22px;top:29px;height:18px;line-height:4px">Feature item<br>Feature item<br>Feature item<br>Feature item</p>
  <p class="p c" style="left:34px;width:22px;top:29px;height:18px;line-height:4px">Feature item<br>Feature item<br>Feature item<br>Feature item</p>
  <p class="p c" style="left:60px;width:22px;top:29px;height:18px;line-height:4px">Feature item<br>Feature item<br>Feature item<br>Feature item</p>
  <p class="p c" style="left:86px;width:22px;top:29px;height:18px;line-height:4px">Feature item<br>Feature item<br>Feature item<br>Feature item</p>
  <p class="p c" style="left:12px;top:50px;width:14px;height:4.5px;border:.6px solid #999;line-height:3.3px">Buy</p>
  <p class="p c" style="left:38px;top:50px;width:14px;height:4.5px;border:.6px solid #999;line-height:3.3px">Buy</p>
  <p class="p c" style="left:64px;top:50px;width:14px;height:4.5px;border:.6px solid #999;line-height:3.3px">Buy</p>
  <p class="p c" style="left:90px;top:50px;width:14px;height:4.5px;border:.6px solid #999;line-height:3.3px">Buy</p>
</div><div class="caption"><span class="num">34</span><span class="meta">★ 00:00</span></div></div>

<!-- 35 -->
<div class="cell"><div class="slide">
  <div class="abs photo-desk" style="inset:0" role="img" aria-label="Photo of potted plants on a bright office desk"></div>
  <div class="abs" style="left:0;right:0;top:33px;height:27px;background:rgba(247,144,30,.88)"></div>
  <div class="hero-text" style="left:12px;top:38px;font-size:7px">TITLE PAGE</div>
  <div class="hero-text" style="left:12px;top:47px;font-size:3px;font-weight:400">YOUR TEXT IS HERE</div>
  <div class="brand big light" style="top:42px;right:12px">NEXORA</div>
</div><div class="caption"><span class="num">35</span></div></div>

</main>
</body>
</html>
```